LVNODE
biz card
LVNODE - Information Technology
Creative Brief
Professional
jun pa
238 Elmora Pl, 3FL NewYorkCity, NY 10583
jun.pa@lanviretnode.com
www.lanviretnode.com

```html
<!DOCTYPE html>
<html lang="en">
<head>
<meta charset="utf-8">
<title>LVNODE Stationery Set</title>
<link rel="stylesheet" href="https://fonts.googleapis.com/css2?family=Open+Sans:wght@400;600;700&display=swap">
<style>
  :root {
    --stage: #9b9b9b;
    --paper: #ffffff;
    --red: #d7262d;
    --red-dark: #a5151b;
    --red-light: #e8474d;
    --ink: #555555;
    --ink-soft: #888888;
  }
  * { margin: 0; padding: 0; box-sizing: border-box; }
  html, body { width: 1200px; height: 684px; overflow: hidden; }
  body {
    background: var(--stage);
    font-family: "Open Sans", Arial, sans-serif;
    position: relative;
  }
  .sheet {
    position: absolute;
    background: var(--paper);
    box-shadow: 0 1px 3px rgba(0,0,0,.25);
    overflow: hidden;
  }
  .band {
    position: absolute; left: 0; right: 0;
    background: linear-gradient(to bottom, var(--red-light), var(--red) 45%, var(--red-dark));
  }
  .band::after {
    content: ""; position: absolute; left: 0; right: 0; height: 2px;
    background: var(--red-dark);
  }
  .band--top { top: 0; }
  .band--top::after { bottom: -4px; }
  .band--bottom { bottom: 0; }
  .band--bottom::after { top: -4px; }
  .brand {
    position: absolute; left: 50%; transform: translateX(-50%);
    display: flex; align-items: center; gap: 6px;
    color: var(--red); font-weight: 700; letter-spacing: .5px;
    white-space: nowrap;
  }
  .brand__mark { background: var(--red); display: block; }
  .contact-line {
    position: absolute; left: 0; right: 0; text-align: center;
    color: var(--ink); white-space: nowrap;
  }
  .site {
    display: flex; align-items: center; justify-content: center; height: 100%;
    color: #fff; font-size: 7px; font-weight: 600;
  }

  /* Business card */
  .card { left: 24px; top: 283px; width: 199px; height: 137px; }
  .card .band--top { height: 24px; }
  .card__name {
    position: relative; z-index: 1; display: block; text-align: center;
    color: #fff; font-size: 9px; font-weight: 600; line-height: 22px;
  }
  .card .band--bottom { height: 12px; }
  .card__contact {
    position: absolute; left: 10px; top: 40px;
    font-size: 5px; line-height: 7px; color: var(--ink);
  }
  .card .brand { top: 84px; font-size: 15px; }
  .card .brand__mark { width: 9px; height: 9px; }
  .card__site { position: absolute; left: 0; right: 0; bottom: 16px; text-align: center; font-size: 5px; color: var(--ink-soft); }

  /* Letterhead */
  .letterhead { left: 259px; top: 12px; width: 382px; height: 650px; }
  .letterhead .band--top { height: 20px; }
  .letterhead .brand { top: 78px; font-size: 22px; }
  .letterhead .brand__mark { width: 13px; height: 13px; }
  .letterhead .contact-line { bottom: 40px; font-size: 5.5px; }
  .letterhead .band--bottom { height: 26px; }

  /* Envelope back */
  .envelope-back { left: 645px; top: 67px; width: 545px; height: 253px; }
  .envelope-back svg { position: absolute; left: 0; top: 0; }

  /* Envelope front */
  .envelope-front { left: 645px; top: 374px; width: 545px; height: 274px; }
  .envelope-front .band--top { height: 20px; }
  .envelope-front .brand { top: 48px; font-size: 22px; }
  .envelope-front .brand__mark { width: 13px; height: 13px; }
  .envelope-front .contact-line { bottom: 38px; font-size: 5.5px; }
  .envelope-front .band--bottom { height: 22px; }
</style>
</head>
<body>

  <section class="sheet card" aria-label="Business card">
    <div class="band band--top"><span class="card__name">jun pa</span></div>
    <div class="card__contact">
      <p>T: 212 555 0142 &nbsp; F: 212 555 0143</p>
      <p>E: jun.pa@lanviretnode.com</p>
      <p>238 Elmora Pl, 3FL NewYorkCity, NY 10583</p>
    </div>
    <div class="brand"><span class="brand__mark"></span>LVNODE</div>
    <p class="card__site">www.lanviretnode.com</p>
    <div class="band band--bottom"></div>
  </section>

  <section class="sheet letterhead" aria-label="Letterhead">
    <div class="band band--top"></div>
    <div class="brand"><span class="brand__mark"></span>LVNODE</div>
    <p class="contact-line">T: 212 555 0142 | F: 212 555 0143 | M: 917 555 0188 | E: jun.pa@lanviretnode.com | A: 238 Elmora Pl, 3FL NewYorkCity, NY 10583</p>
    <div class="band band--bottom"><span class="site">www.lanviretnode.com</span></div>
  </section>

  <section class="sheet envelope-back" aria-label="Envelope back">
    <svg width="545" height="253" viewBox="0 0 545 253" aria-hidden="true">
      <defs>
        <radialGradient id="flapFill" cx="50%" cy="20%" r="70%">
          <stop offset="0" stop-color="#e8474d"/>
          <stop offset="0.6" stop-color="#d7262d"/>
          <stop offset="1" stop-color="#a5151b"/>
        </radialGradient>
      </defs>
      <path d="M0 0 H545 V72 Q545 92 525 92 H20 Q0 92 0 72 Z" fill="url(#flapFill)"/>
    </svg>
  </section>

  <section class="sheet envelope-front" aria-label="Envelope front">
    <div class="band band--top"></div>
    <div class="brand"><span class="brand__mark"></span>LVNODE</div>
    <p class="contact-line">T: 212 555 0142 | F: 212 555 0143 | M: 917 555 0188 | E: jun.pa@lanviretnode.com | A: 238 Elmora Pl, 3FL NewYorkCity, NY 10583</p>
    <div class="band band--bottom"><span class="site">www.lanviretnode.com</span></div>
  </section>

</body>
</html>
```